Veloran Dental Development - Business Cards

We are a Dental Development and Management company. We are looking to develop a new business card design. We are business professional but modern. The logo that I have attached is the business colors. You can also check out our website for further detail. www.veloranmgmt-example.com

Target Market(s)

Dental Professionals, Dentists and Office Staff, Marketing Professionals

Industry/Entity Type

Business

Requirements
Must have
• Name - Bartholomew K. Tressing
Title - Marketing Director
Phone - 555-019-4827
Cell - 555-019-4827
Email - Bart.t@veloran-example.com
Address - 2917 W Larkmoor Rd, Mesa, AZ 85209
Web- www.veloran-example.com

Veloran Logo must go on the front. The other logos go on the back as affiliated businesses

Must be editable to enter specific Names, Positions, Phone numbers and email later on. Using Adobe CS5 currently.

```html
<!DOCTYPE html>
<html lang="en">
<head>
<meta charset="utf-8">
<title>Veloran Dental Development – Business Cards</title>
<link rel="stylesheet" href="https://fonts.googleapis.com/css2?family=Libre+Baskerville:wght@400;700&family=Arimo:wght@700&display=swap">
<style>
  :root {
    --navy: #27306a;
    --gold: #e0992a;
    --gold-soft: #eecf9e;
    --lilac: #b8b6cf;
    --card: #ffffff;
    --backdrop: #f2f2f2;
    --serif: "Libre Baskerville", Georgia, serif;
    --sans: "Arimo", Arial, sans-serif;
  }
  html, body {
    margin: 0;
    padding: 0;
    overflow: hidden;
  }
  body {
    width: 1200px;
    height: 1000px;
    background: var(--backdrop);
    position: relative;
  }
  .card {
    position: absolute;
    top: 379px;
    width: 391px;
    height: 242px;
    background: var(--card);
    box-shadow: 0 1px 3px rgba(0,0,0,.12);
    overflow: hidden;
  }
  .card--front { left: 192px; }
  .card--back  { left: 619px; }

  .wash {
    position: absolute;
    right: 0;
    bottom: 0;
    width: 320px;
    height: 135px;
    background: radial-gradient(ellipse at 100% 100%, rgba(238,207,158,.55) 0%, rgba(184,182,207,.35) 45%, rgba(255,255,255,0) 75%);
  }

  .brand {
    position: absolute;
    left: 28px;
    top: 42px;
    font-family: var(--serif);
    color: var(--navy);
  }
  .brand__name {
    font-size: 30px;
    font-weight: 400;
    letter-spacing: 1px;
    text-transform: uppercase;
    margin: 0;
    line-height: 1;
  }
  .brand__tag {
    font-family: var(--sans);
    color: var(--gold);
    font-size: 12.5px;
    letter-spacing: 2px;
    margin: 8px 0 0 42px;
    text-transform: uppercase;
  }

  .person {
    position: absolute;
    left: 18px;
    top: 122px;
    font-family: var(--serif);
  }
  .person__name {
    margin: 0;
    font-size: 14.5px;
    font-weight: 700;
    color: var(--navy);
  }
  .person__title {
    margin: 4px 0 0;
    font-size: 11.5px;
    color: var(--gold);
  }

  .contact {
    position: absolute;
    right: 18px;
    top: 162px;
    margin: 0;
    padding: 0;
    list-style: none;
    text-align: right;
    font-family: var(--sans);
    font-size: 10px;
    line-height: 13.3px;
    font-weight: 700;
  }
  .contact__label { color: var(--navy); margin-right: 3px; }
  .contact__value { color: var(--gold); }

  .affiliate {
    position: absolute;
    font-family: var(--serif);
    font-weight: 700;
    font-size: 15px;
    line-height: 1.2;
    color: var(--navy);
    display: flex;
    align-items: center;
    gap: 8px;
  }
  .affiliate__mark {
    flex: none;
    width: 20px;
    height: 20px;
    background: var(--gold);
    border-radius: 50%;
  }
  .affiliate__mark--square { border-radius: 0; }
  .affiliate--centers { left: 42px;  top: 42px; width: 150px; }
  .affiliate--plan    { left: 218px; top: 42px; width: 150px; }
  .affiliate--urgent  { left: 24px;  top: 150px; width: 170px; }
  .affiliate--kids    { left: 218px; top: 150px; width: 150px; }
</style>
</head>
<body>

<section class="card card--front" aria-label="Business card front">
  <div class="wash"></div>
  <div class="brand">
    <p class="brand__name">Veloran</p>
    <p class="brand__tag">Dental Development</p>
  </div>
  <div class="person">
    <p class="person__name">Bartholomew K. Tressing</p>
    <p class="person__title">Marketing Director</p>
  </div>
  <ul class="contact">
    <li><span class="contact__label">p.</span><span class="contact__value">555-019-4827</span></li>
    <li><span class="contact__label">c.</span><span class="contact__value">555-019-4827</span></li>
    <li><span class="contact__label">e.</span><span class="contact__value">Bart.t@veloran-example.com</span></li>
    <li><span class="contact__label">a.</span><span class="contact__value">2917 W Larkmoor Rd, Mesa, AZ 85209</span></li>
    <li><span class="contact__label">w.</span><span class="contact__value">www.veloran-example.com</span></li>
  </ul>
</section>

<section class="card card--back" aria-label="Business card back with affiliated businesses">
  <div class="wash"></div>
  <div class="affiliate affiliate--centers"><span class="affiliate__mark"></span>Hearthside Dental Centers</div>
  <div class="affiliate affiliate--plan"><span class="affiliate__mark"></span>Hearthside Dental Plan</div>
  <div class="affiliate affiliate--urgent"><span class="affiliate__mark affiliate__mark--square"></span>Rapidcare Dental Centers</div>
  <div class="affiliate affiliate--kids"><span class="affiliate__mark"></span>Sproutsmile Pediatric Dental</div>
</section>

</body>
</html>
```